Web Site for Strategy and Technology Consulting Company

We are looking for a website design that engages potential customers to understand our services and contact us. In this contest, we are looking for a homepage design, but the winning designer will be favored for the design of some of the more complicated interior pages of the site. An additional contest (or contests) for these pages will be added soon.

PLATROM AND RESPONSIVE DESIGN
The site will be implemented in WordPress using the Elementor page builder.
We are looking for a design that will look good on phones are well as laptop browsers.

UPLOADED FILES INCLUDE:
1a A wireframe of the homepage we are looking for. The Uploaded PDF also includes a draft of the text proposed for the homepage. Designers are free to go beyond the wireframe, but all elements of the wireframe should be included.
1b A Word document with the draft text of the homepage.
2a-d The Norvalith logo. Two versions are included – a dark version which works well against a light background, and a light version which works well against a dark background.
3 The Norvalith color palette with HEX and RGB values. Designers are not limited to this palette, but colors should be complementary.
4 A draft of the homepage menu
5 Service sheets with information on the services we provide

MORE ABOUT NORVALITH
Norvalith is a consulting company focused on transforming businesses through software. Our tagline, “Transformation Delivered,” recognizes the gap business often have between business transformation and the software they end up with. By listening to our customers and understanding their vision and where they are, we help get our customers where they want to go.

We increase our capability by working with many consultants and partners, allowing us to provide our customers with the best people and the software that best suits them.

Industry/Entity Type

Consulting

Number of Pages Required

1 page

Font styles to use
Sans Serif

Requirements
Must have
• the content represented on the wireframe uploaded
Nice to have
• interactive features, such as roll-over icons that reveal additional information

```html
<!DOCTYPE html>
<html lang="en">
<head>
<meta charset="utf-8">
<title>Norvalith — Transformation Delivered</title>
<link href="https://fonts.googleapis.com/css2?family=Inter:wght@400;500;600;700&display=swap" rel="stylesheet">
<style>
:root{
  --navy:#17375f;
  --navy-deep:#0a1628;
  --ink:#1c2a48;
  --body:#4d5874;
  --muted:#8a94ab;
  --yellow:#e6c53a;
  --pill:#e4edf9;
  --pill-text:#2c5a9a;
  --pale:#eef3fa;
  --line:#e6eaf1;
  --white:#ffffff;
  --accent:#3b73d4;
}
*{box-sizing:border-box;margin:0;padding:0}
html,body{width:1200px;height:4519px;overflow:hidden}
body{position:relative;background:var(--white);font-family:'Inter',sans-serif;color:var(--body);font-size:13px;line-height:1.55}
.abs{position:absolute}
.pill{display:inline-block;background:var(--pill);color:var(--pill-text);font-size:11px;padding:4px 18px;border-radius:20px}
.btn{display:inline-flex;align-items:center;justify-content:center;gap:10px;height:32px;border-radius:16px;font-size:11px;text-decoration:none}
.btn-yellow{background:var(--yellow);color:var(--white)}
.btn-ghost{background:rgba(255,255,255,.18);color:var(--white)}
h2.section-title{font-weight:500;color:var(--ink);font-size:31px;letter-spacing:-1px;line-height:1.18}

/* header / hero */
.hero{left:0;top:0;width:1200px;height:623px}
.hero-photo{position:absolute;inset:0;background:linear-gradient(110deg,#2a4f7d 0%,#4c6f96 40%,#2d4a72 70%,#1d3558 100%);clip-path:polygon(0 0,100% 0,100% 553px,0 623px)}
.logo{font-weight:500;font-size:24px;letter-spacing:-.5px;color:var(--white)}
.nav{top:14px;left:0;width:1200px;height:30px}
.nav .logo{position:absolute;left:119px;top:0}
.nav-links{position:absolute;left:602px;top:8px;display:flex;gap:0}
.nav-links a{color:var(--white);font-size:12px;text-decoration:none;margin-right:48px}
.nav .btn{position:absolute;left:974px;top:0;width:105px;height:30px}
.hero-copy{left:119px;top:170px;width:560px}
.hero-copy .pill{background:rgba(255,255,255,.16);color:var(--white);font-size:10px}
.hero-copy h1{color:var(--white);font-weight:500;font-size:48px;letter-spacing:-1.8px;line-height:1.1;margin:14px 0 16px}
.hero-copy p{color:#e4ebf5;font-size:12px;line-height:1.55;width:560px}
.hero-actions{display:flex;gap:25px;margin-top:26px}
.scroll-hint{left:590px;top:508px}

/* services intro */
.intro{left:0;top:682px;width:1200px;text-align:center}
.intro p{width:570px;margin:12px auto 0;font-size:12px}
.intro-photo{left:119px;top:865px;width:366px;height:338px;background:linear-gradient(135deg,#c9d3de,#8fa2b8 60%,#5d6f86)}
.features{left:610px;top:875px;width:420px}
.feature{display:flex;gap:16px;margin-bottom:40px}
.feature .ic{width:32px;height:32px;flex:none;border-radius:50%;display:flex;align-items:center;justify-content:center}
.feature h3,.talent-item h3{font-size:13px;font-weight:600;color:var(--ink);margin-bottom:4px}
.feature p,.talent-item p{font-size:11.5px;line-height:1.6}

/* solutions */
.solutions-head{left:119px;top:1388px}
.solutions-head h2{margin-top:12px}
.solutions-lead{left:609px;top:1428px;width:455px;font-size:11.5px;line-height:1.6}
.card{position:absolute;width:307px;height:209px;background:var(--white);border:1px solid var(--line);border-radius:3px;padding:28px 30px}
.card h3{font-size:12.5px;font-weight:600;color:var(--ink);margin:14px 0 14px}
.card p{font-size:11.5px;line-height:1.6}
.card-cta{background:linear-gradient(150deg,#0f2a4d,#1c4a7d 60%,#0d2340);border:none;color:var(--white);padding:30px 30px}
.card-cta h3{color:var(--white);margin:0 0 10px;font-size:13px;line-height:1.4}
.card-cta p{color:#dbe4f1;margin-bottom:14px}
.card-cta .btn{width:122px;height:30px}

/* talent */
.talent-photo{left:114px;top:2200px;width:404px;height:492px;background:linear-gradient(160deg,#8a8f93,#b59d86 45%,#5b6671)}
.talent{left:608px;top:2206px;width:450px}
.talent h2{margin:10px 0 14px}
.talent > p{font-size:11.5px;line-height:1.6;margin-bottom:52px}
.talent-item{display:flex;gap:16px;margin-bottom:36px}
.talent-box{left:605px;top:2578px;width:470px;height:111px;background:var(--pale);border-radius:3px;padding:18px 18px}
.talent-box p{font-size:10.5px;line-height:1.7;margin-bottom:10px}
.talent-box .btn{width:122px;height:30px}

/* testimonials */
.testi-bg{left:0;top:2870px;width:1200px;height:1270px;background:var(--pale);clip-path:polygon(0 0,100% 90px,100% 1160px,0 1265px)}
.testi-head{left:119px;top:3040px}
.testi-head h2{margin:10px 0 10px}
.testi-head p{font-size:11.5px;line-height:1.6;width:470px}
.testi-track{left:119px;top:3189px;width:1081px;height:270px;overflow:hidden}
.testi-card{position:absolute;top:0;width:374px;height:263px;background:var(--white);border-radius:4px;padding:36px 40px}
.testi-card h3{font-size:15px;font-weight:500;color:var(--ink);margin-bottom:16px}
.testi-card p{font-size:11px;line-height:2.05}
.person{display:flex;gap:14px;align-items:center;margin-top:16px}
.avatar{width:44px;height:44px;border-radius:50%;background:linear-gradient(135deg,#e6d6e8,#c2b6d4)}
.person b{display:block;font-size:12.5px;font-weight:600;color:var(--ink)}
.person span{font-size:11px;color:var(--muted)}
.fade{position:absolute;right:0;top:0;width:120px;height:263px;background:linear-gradient(90deg,rgba(255,255,255,0),rgba(238,243,250,.95))}
.next{left:1087px;top:3300px;width:42px;height:42px;border-radius:50%;background:var(--yellow)}

/* technologies */
.tech-title{left:0;top:3705px;width:1200px;text-align:center}
.tech-row{left:56px;top:3800px;width:1100px;display:flex;justify-content:space-between;align-items:center}
.tech{display:flex;align-items:center;gap:10px;color:#9aa2b2;font-size:16px;font-weight:500}
.tech i{display:block;width:26px;height:26px;background:#b8bfcb}

/* footer */
.footer-bg{left:0;top:3945px;width:1200px;height:574px;background:linear-gradient(180deg,#07111f,#0c2242 60%,#143563);clip-path:polygon(0 72px,100% 0,100% 100%,0 100%)}
.cta{left:0;top:4088px;width:1200px;text-align:center;color:var(--white)}
.cta h2{font-size:29px;font-weight:500;letter-spacing:-1px;color:var(--white)}
.cta p{font-size:11.5px;color:#d7e0ee;margin:6px 0 16px}
.cta .btn{width:122px}
.foot-brand{left:119px;top:4290px;width:230px}
.foot-brand p{color:#c9d4e5;font-size:10.5px;line-height:1.7;margin-top:8px}
.socials{display:flex;gap:12px;margin-top:18px}
.socials span{width:24px;height:24px;border-radius:50%;background:#2b4c86}
.foot-col{top:4296px;color:#c9d4e5;font-size:10.5px}
.foot-col h4{color:var(--white);font-size:12px;font-weight:600;margin-bottom:14px}
.foot-col a{display:block;color:#c9d4e5;text-decoration:none;margin-bottom:9px}
.foot-col address{font-style:normal;line-height:1.75}
.foot-line{left:119px;top:4482px;width:962px;height:1px;background:rgba(255,255,255,.15)}
.copyright{left:0;top:4492px;width:1200px;text-align:center;color:#aab6c9;font-size:9.5px}
</style>
</head>
<body>

<!-- Hero -->
<section class="abs hero">
  <div class="hero-photo" role="img" aria-label="Photo of business professionals in a bright office, tinted blue"></div>
  <header class="abs nav">
    <div class="logo">Norvalith</div>
    <nav class="nav-links"><a href="#">About Us</a><a href="#">Services</a><a href="#">Insights</a><a href="#">Join Us</a></nav>
    <a class="btn btn-yellow" href="#">Let's Talk</a>
  </header>
  <div class="abs hero-copy">
    <span class="pill">Empowering your transformation journey</span>
    <h1>Innovate for a better<br>business future</h1>
    <p>At Norvalith, we go beyond software implementation. We prioritize listening to our customers, understanding their unique transformation journeys, and supporting their vision for the future. Our partnership is built on removing obstacles and ensuring they achieve their goals.</p>
    <div class="hero-actions">
      <a class="btn btn-yellow" href="#" style="width:121px">Let's Talk
        <svg width="16" height="8" viewBox="0 0 16 8"><path d="M0 4h14M11 1l3 3-3 3" stroke="#fff" fill="none" stroke-width="1.2"/></svg></a>
      <a class="btn btn-ghost" href="#" style="width:116px">Learn More</a>
    </div>
  </div>
  <svg class="abs scroll-hint" width="18" height="34" viewBox="0 0 18 34" aria-hidden="true">
    <rect x="4" y="1" width="10" height="16" rx="5" stroke="#fff" fill="none" stroke-width="1.2"/>
    <line x1="9" y1="5" x2="9" y2="9" stroke="#fff" stroke-width="1.2"/>
    <path d="M5 22l4 4 4-4M5 27l4 4 4-4" stroke="#fff" fill="none" stroke-width="1"/>
  </svg>
</section>

<!-- Services intro -->
<section class="abs intro">
  <h2 class="section-title">Discover the power of our superior services</h2>
  <p>At Norvalith, we go beyond software implementation. We prioritize listening to our customers, understanding their unique transformation journeys, and supporting their vision for the future. Our partnership is built on removing obstacles and ensuring they achieve their goals.</p>
</section>
<div class="abs intro-photo" role="img" aria-label="Photo of two colleagues smiling at a meeting table"></div>
<div class="abs features">
  <div class="feature"><div class="ic" style="background:#fdf3d6"><svg width="18" height="18" viewBox="0 0 18 18"><circle cx="9" cy="9" r="6" stroke="#e6b52a" fill="none" stroke-width="1.5"/><circle cx="9" cy="9" r="2" fill="#e6b52a"/></svg></div>
    <div><h3>Emphasis on business value</h3><p>We focus on delivering tangible value swiftly, helping you realize the benefits of your transformation initiatives.</p></div></div>
  <div class="feature"><div class="ic" style="background:#fde7d6"><svg width="18" height="18" viewBox="0 0 18 18"><path d="M3 9l4-4 3 3 5-3-3 8-4 1z" fill="#f0a35b"/></svg></div>
    <div><h3>Meeting you where you are</h3><p>We meet our customers at their current stage of transformation, avoiding unnecessary setbacks or rework.</p></div></div>
  <div class="feature"><div class="ic" style="background:#dde9fb"><svg width="18" height="18" viewBox="0 0 18 18"><circle cx="9" cy="9" r="6.5" stroke="var(--accent)" fill="none" stroke-width="1.5"/><circle cx="9" cy="9" r="2.5" fill="var(--accent)"/></svg></div>
    <div><h3>Comprehensive services</h3><p>From strategic planning to ongoing product support, we provide a comprehensive suite of services for your needs.</p></div></div>
  <div class="feature"><div class="ic" style="background:#e1f4df"><svg width="18" height="18" viewBox="0 0 18 18"><path d="M4 14l3-7 7-3-3 7z" fill="#3aa84a"/></svg></div>
    <div><h3>Committed to long-term success</h3><p>Our dedication extends beyond immediate outcomes; we are invested in your long-term success.</p></div></div>
</div>

<!-- Solutions -->
<div class="abs solutions-head">
  <span class="pill">Our Solutions</span>
  <h2 class="section-title">Integrated solutions for your<br>transformation journey</h2>
</div>
<p class="abs solutions-lead">At Norvalith, we understand that successful business transformation goes hand in hand with quality software implementations. We have evolved to focus on five essential elements that businesses need to achieve their goals:</p>

<article class="card" style="left:119px;top:1552px">
  <svg width="38" height="38" viewBox="0 0 38 38"><rect x="4" y="6" width="24" height="28" rx="2" stroke="#e6b52a" fill="none" stroke-width="2"/><path d="M10 26l16-16 4 4-16 16h-4z" fill="#f3d36a"/></svg>
  <h3>Business Transformation</h3>
  <p>We help define and execute your transformation strategy, ensuring it aligns with your unique objectives and industry landscape.</p>
</article>
<article class="card" style="left:446px;top:1552px">
  <svg width="44" height="38" viewBox="0 0 44 38"><circle cx="14" cy="22" r="8" stroke="var(--accent)" fill="none" stroke-width="2" stroke-dasharray="3 2"/><circle cx="30" cy="14" r="6" stroke="var(--accent)" fill="none" stroke-width="2" stroke-dasharray="3 2"/><circle cx="14" cy="22" r="3" fill="var(--accent)"/></svg>
  <h3>ERP Implementations</h3>
  <p>We assess, upgrade, and implement ERP solutions that are tailored to your specific requirements, enabling seamless operations and improved efficiency.</p>
</article>
<article class="card" style="left:772px;top:1552px">
  <svg width="40" height="38" viewBox="0 0 40 38"><circle cx="8" cy="8" r="4" fill="#3aa84a"/><circle cx="20" cy="6" r="4" fill="#3aa84a"/><circle cx="32" cy="8" r="4" fill="#3aa84a"/><path d="M14 34V18l6 4 6-4v16z" stroke="#3aa84a" fill="none" stroke-width="2"/></svg>
  <h3>CRM Implementations</h3>
  <p>Take your customer relationships to the next level with customized CRM solutions that optimize engagement and drive growth.</p>
</article>
<article class="card" style="left:119px;top:1780px">
  <svg width="40" height="40" viewBox="0 0 40 40"><rect x="4" y="4" width="32" height="20" fill="none" stroke="#e04fc0" stroke-width="2" stroke-dasharray="2 2"/><path d="M20 24v12M14 30h12" stroke="#e04fc0" stroke-width="2"/></svg>
  <h3>BI and Data</h3>
  <p>Discover, connect, and trust your data through robust business intelligence solutions, unlocking valuable insights to support informed decision-making.</p>
</article>
<article class="card" style="left:446px;top:1780px">
  <svg width="40" height="40" viewBox="0 0 40 40"><path d="M6 6l28 28M34 6L6 34M20 4v32M4 20h32" stroke="var(--navy)" stroke-width="1.6"/><circle cx="20" cy="20" r="6" fill="none" stroke="var(--accent)" stroke-width="2"/></svg>
  <h3>Building the Right Team of People</h3>
  <p>As your transformation partner, we aid in recruiting and hiring the skilled resources needed to support and drive your journey forward.</p>
</article>
<article class="card card-cta" style="left:772px;top:1780px">
  <h3>Learn How Norvalith Can<br>Accelerate Your Transformation</h3>
  <p>Let us help you navigate the complexities and ensure successful outcomes for your business.</p>
  <a class="btn btn-yellow" href="#">Let's Talk
    <svg width="16" height="8" viewBox="0 0 16 8"><path d="M0 4h14M11 1l3 3-3 3" stroke="#fff" fill="none" stroke-width="1.2"/></svg></a>
</article>

<!-- Talent -->
<div class="abs talent-photo" role="img" aria-label="Photo of three smiling colleagues gathered around a laptop"></div>
<section class="abs talent">
  <span class="pill">Our Team</span>
  <h2 class="section-title">Our talent pool</h2>
  <p>The world has changed in the past twenty years. The people you need might not all work for one company. Our clients want the best resources, available quickly. That's why, in addition to our team of experts, we partner with:</p>
  <div class="talent-item"><div class="ic" style="width:32px;height:32px;flex:none;border-radius:50%;background:#e1f4df;display:flex;align-items:center;justify-content:center"><svg width="18" height="18" viewBox="0 0 18 18"><circle cx="9" cy="6" r="3" fill="#3aa84a"/><path d="M3 16c0-4 12-4 12 0z" fill="#3aa84a"/></svg></div>
    <div><h3>Expert Consultants</h3><p>Our network of skilled consultants excels in their respective fields, ensuring you have the best talent working on your projects.</p></div></div>
  <div class="talent-item"><div class="ic" style="width:32px;height:32px;flex:none;border-radius:50%;background:#dde9fb;display:flex;align-items:center;justify-content:center"><svg width="18" height="18" viewBox="0 0 18 18"><circle cx="9" cy="9" r="6.5" stroke="var(--accent)" fill="none" stroke-width="1.4"/><path d="M2.5 9h13M9 2.5c3 3 3 10 0 13M9 2.5c-3 3-3 10 0 13" stroke="var(--accent)" fill="none" stroke-width="1"/></svg></div>
    <div><h3>Global Service Providers</h3><p>We collaborate with service providers worldwide, offering resources and value that align with your specific needs, available 24/7.</p></div></div>
</section>
<div class="abs talent-box">
  <p>Discover how our experts can seamlessly integrate with your team, amplifying your capabilities and driving your accomplishments forward.</p>
  <a class="btn btn-yellow" href="#">Our team
    <svg width="16" height="8" viewBox="0 0 16 8"><path d="M0 4h14M11 1l3 3-3 3" stroke="#fff" fill="none" stroke-width="1.2"/></svg></a>
</div>

<!-- Testimonials -->
<div class="abs testi-bg"></div>
<div class="abs testi-head">
  <span class="pill" style="background:var(--white)">Testimonials</span>
  <h2 class="section-title">Hear what our clients say</h2>
  <p>Discover How Norvalith's Transformation Solutions Have Impacted Businesses Across Industries, Empowering Growth and Success.</p>
</div>
<div class="abs testi-track">
  <article class="testi-card" style="left:0">
    <h3>"Game-Changing Transformation"</h3>
    <p>We partnered with Norvalith for our digital transformation, and the results were phenomenal. Their expertise and support propelled our business to new heights, exceeding our expectations.</p>
    <div class="person"><div class="avatar" role="img" aria-label="Client portrait"></div><div><b>Lena Harlow</b><span>CEO at Brightfield Agency</span></div></div>
  </article>
  <article class="testi-card" style="left:398px">
    <h3>"Unparalleled Support and Expertise"</h3>
    <p>Norvalith provided unparalleled support throughout our ERP implementation. Their team's expertise and dedication ensured a seamless transition, enabling us to streamline operations and drive efficiency.</p>
    <div class="person"><div class="avatar" role="img" aria-label="Client portrait"></div><div><b>Owen Calder</b><span>Project Manager at Parcelwise</span></div></div>
  </article>
  <article class="testi-card" style="left:795px">
    <h3>"Unparalleled Support and Results"</h3>
    <p>Working with Norvalith was a game-changer for our organization. Their guidance and team helped us navigate complex change and allowed us to achieve our goals faster.</p>
    <div class="person"><div class="avatar" role="img" aria-label="Client portrait"></div><div><b>Reid Thornton</b><span>Developer at Quellsoft</span></div></div>
    <div class="fade"></div>
  </article>
</div>
<svg class="abs next" viewBox="0 0 42 42" aria-label="Next testimonial"><path d="M18 14l7 7-7 7" stroke="#fff" fill="none" stroke-width="2"/></svg>

<!-- Technologies -->
<h2 class="abs tech-title section-title">Technologies</h2>
<div class="abs tech-row">
  <div class="tech"><i></i>Corvex Suite</div>
  <div class="tech">Orellan BI</div>
  <div class="tech">Tallowbay</div>
  <div class="tech"><i style="width:20px;height:20px"></i>Quadrix</div>
  <div class="tech">Tallowbay Prism</div>
</div>

<!-- Footer -->
<div class="abs footer-bg"></div>
<section class="abs cta">
  <h2>Have a project in mind? Let's talk</h2>
  <p>Connect with us to discuss your project and start your transformation journey today</p>
  <a class="btn btn-yellow" href="#">Let's Talk
    <svg width="16" height="8" viewBox="0 0 16 8"><path d="M0 4h14M11 1l3 3-3 3" stroke="#fff" fill="none" stroke-width="1.2"/></svg></a>
</section>
<div class="abs foot-brand">
  <div class="logo">Norvalith</div>
  <p>Technology and innovation consultants driving enduring transformation via global horsepower with a human touch.</p>
  <div class="socials" aria-label="Social links"><span></span><span></span><span></span><span></span></div>
</div>
<div class="abs foot-col" style="left:491px"><h4>Useful Links</h4><a href="#">About Us</a><a href="#">Services</a><a href="#">Insights</a><a href="#">Join Us</a></div>
<div class="abs foot-col" style="left:652px"><h4>Support</h4><a href="#">Privacy Policy</a><a href="#">Terms and Conditions</a><a href="#">Help and Support</a><a href="#">Contact Us</a></div>
<div class="abs foot-col" style="left:852px;width:230px"><h4>Find Us</h4>
  <address>410 Lakeview Plaza<br>Suite 218,<br>Brookhaven, MN<br>55990<br>PH: (555) 014-2278<br>EMAIL: hello@norvalith-consulting.example</address></div>
<div class="abs foot-line"></div>
<p class="abs copyright">© 2023 Norvalith. All rights reserved.</p>

</body>
</html>
```